Design a business card

Our client's current business cards are not very professional. We would like a new, modern looking business card template created. The files submitted should be either Photoshop or Illustrator and a PDF version. The company website is www.tessalinesystems.com. I have attached a photo of the current business card so you have the required information.

We would like the back to have some feature (color, website, etc.)

Company name is

Tessaline Systems, Inc

```html
<!DOCTYPE html>
<html lang="en">
<head>
<meta charset="utf-8">
<title>Tessaline Systems, Inc — Business Card</title>
<link href="https://fonts.googleapis.com/css2?family=EB+Garamond:wght@400;600;700&display=swap" rel="stylesheet">
<style>
  :root {
    --teal: #1a8f9c;
    --aqua: #2bbcd0;
    --charcoal: #333538;
    --slate: #5a5d61;
    --ink: #1d1d1f;
    --paper: #ffffff;
    --backdrop: #e9ecef;
  }
  * { box-sizing: border-box; margin: 0; padding: 0; }
  html, body { width: 1200px; height: 900px; overflow: hidden; }
  body {
    background: var(--backdrop);
    font-family: "EB Garamond", Georgia, serif;
    color: var(--ink);
    position: relative;
  }
  .card {
    position: absolute;
    width: 520px;
    height: 300px;
    top: 300px;
    background: var(--paper);
    border-radius: 18px;
    overflow: hidden;
    box-shadow: 0 10px 30px rgba(0,0,0,0.15);
  }
  .card--front { left: 50px; }
  .card--back { left: 630px; }
  .card__shapes { position: absolute; inset: 0; }

  /* Front */
  .brand {
    position: absolute;
    display: flex;
    flex-direction: column;
    align-items: center;
    gap: 8px;
    color: var(--paper);
  }
  .brand__mark {
    width: 44px; height: 44px;
    border-radius: 50%;
    background: var(--paper);
  }
  .brand__name {
    font-size: 26px;
    font-weight: 400;
    line-height: 1.05;
    text-align: center;
  }
  .card--front .brand { left: 22px; top: 40px; width: 170px; }

  .person {
    position: absolute;
    right: 36px; top: 52px;
    text-align: right;
  }
  .person__name { font-size: 30px; font-weight: 700; line-height: 1; }
  .person__title {
    font-size: 13px; letter-spacing: 3.5px; margin-top: 4px;
  }
  .contacts {
    position: absolute;
    right: 30px; bottom: 22px;
    list-style: none;
    font-size: 14px;
    text-align: right;
  }
  .contacts li {
    display: flex; justify-content: flex-end; align-items: center;
    gap: 8px; line-height: 22px;
  }
  .contacts svg { width: 12px; height: 12px; fill: var(--teal); flex: none; }

  /* Back */
  .card--back .brand {
    left: 0; right: 0; top: 40px; color: var(--ink);
  }
  .card--back .brand__mark { background: var(--teal); }
  .card--back .brand__name { font-size: 28px; font-weight: 700; }
  .services {
    position: absolute; left: 40px; right: 40px; top: 162px;
  }
  .services__label {
    display: block; width: max-content; margin: 0 auto 8px;
    background: var(--teal); color: var(--paper);
    font-size: 13px; padding: 0 8px; line-height: 18px;
  }
  .services__list {
    list-style: none;
    display: grid; grid-template-columns: repeat(3, auto);
    justify-content: space-between;
    font-size: 13.5px; row-gap: 2px;
  }
  .services__list li::before { content: "\25C6\00a0"; font-size: 9px; vertical-align: 1px; }
  .back-band {
    position: absolute; left: 0; right: 0; bottom: 0; height: 30px;
    background: var(--aqua);
  }
  .back-tab {
    position: absolute; right: 40px; top: 0; width: 90px; height: 30px;
    background: linear-gradient(90deg, var(--slate) 0 35%, var(--charcoal) 35%);
  }
</style>
</head>
<body>
  <section class="card card--front" aria-label="Card front">
    <svg class="card__shapes" viewBox="0 0 520 300" aria-hidden="true">
      <polygon points="0,0 250,0 180,300 0,300" fill="var(--teal)"/>
      <polygon points="250,0 290,0 282,34 242,34" fill="var(--charcoal)"/>
      <polygon points="0,220 200,220 196,236 0,236" fill="var(--charcoal)" opacity="0.9"/>
    </svg>
    <div class="brand">
      <span class="brand__mark"></span>
      <span class="brand__name">Tessaline<br>Systems, Inc</span>
    </div>
    <div class="person">
      <h1 class="person__name">Marek Holloway</h1>
      <p class="person__title">Software Engineer</p>
    </div>
    <ul class="contacts">
      <li>(555) 310-4200 <svg viewBox="0 0 12 12"><path d="M2 1l2 0 1 3-1.5 1a6 6 0 0 0 3 3L7.5 6.5l3 1v2a1 1 0 0 1-1 1A9 9 0 0 1 1 2a1 1 0 0 1 1-1z"/></svg></li>
      <li>(555) 310-4233 <svg viewBox="0 0 12 12"><rect x="1" y="4" width="10" height="6" rx="1"/><rect x="3" y="1" width="6" height="3"/></svg></li>
      <li>(555) 846-0197 <svg viewBox="0 0 12 12"><rect x="3" y="0.5" width="6" height="11" rx="1"/></svg></li>
      <li>mholloway@tessalinesystems.com <svg viewBox="0 0 12 12"><path d="M1 2.5h10v7H1z M1 2.5l5 4 5-4" stroke="#fff" stroke-width="0.8"/></svg></li>
      <li>www.tessalinesystems.com <svg viewBox="0 0 12 12"><circle cx="6" cy="6" r="5"/></svg></li>
      <li>2210 Larkin Ave. Suite B Brookfield, IL 60599 <svg viewBox="0 0 12 12"><path d="M6 0.5a4 4 0 0 1 4 4c0 3-4 7-4 7s-4-4-4-7a4 4 0 0 1 4-4z"/></svg></li>
    </ul>
  </section>

  <section class="card card--back" aria-label="Card back">
    <div class="back-tab"></div>
    <div class="brand">
      <span class="brand__mark"></span>
      <span class="brand__name">Tessaline Systems, Inc</span>
    </div>
    <div class="services">
      <span class="services__label">Services</span>
      <ul class="services__list">
        <li>Gamma Scanning</li>
        <li>Water Treatment</li>
        <li>Radiation Protection</li>
        <li>Online Fuel Inspection</li>
        <li>Noble Metals Sampling</li>
        <li>Pilot Plant</li>
        <li></li>
        <li>Media Testing</li>
      </ul>
    </div>
    <div class="back-band"></div>
  </section>
</body>
</html>
```